Business Card Design Project - Sports Brand

Brisk is a e-commerce fitness wear brand for ladies who are into gym, pole and swim.

Card should not be overly cluttered and should include the following:

1. logo
2. Name of the company (Use "Brisk Loom Pte Ltd" for now)
3. Address of company (Use a mock address)
4. Representative's name and contact info etc. (use a mock name and contact info)
5. website address

Target Market(s)

Women who are into pole , gym, and swim.

Women who shop online

Industry/Entity Type

E-Commerce

Colors

Designer to choose colors to be used in the design.

Requirements
Nice to have
• feminine sublimation of colours

Need not be printed on traditional paper. We would like the design to be revolutionary and interesting to the eye :)
Should not have
• the design should not be traditional looking. Do not include illustrations of Bikinis, yoga poses etc. in the card.

```html
<!DOCTYPE html>
<html lang="en">
<head>
<meta charset="utf-8">
<title>Brisk Loom Pte Ltd – Business Card</title>
<link href="https://fonts.googleapis.com/css2?family=PT+Sans+Narrow&family=PT+Serif:wght@400;700&display=swap" rel="stylesheet">
<style>
  :root {
    --backdrop: #ece9e6;
    --card: #ffffff;
    --ink: #1e1e1e;
    --muted: #7a7a7a;
    --brand-red: #c8253f;
    --wash-pink: #e9577d;
    --wash-light: #f4a3b6;
    --wash-orange: #f28a5a;
  }
  * { margin: 0; padding: 0; box-sizing: border-box; }
  html, body { width: 1200px; height: 800px; overflow: hidden; }
  body {
    background: var(--backdrop);
    display: flex;
    align-items: center;
    justify-content: center;
    gap: 40px;
  }
  .card {
    position: relative;
    width: 540px;
    height: 310px;
    background: var(--card);
    box-shadow: 0 6px 18px rgba(0,0,0,0.12);
    overflow: hidden;
  }

  /* Contact side */
  .contact-wash {
    position: absolute;
    top: 0;
    right: 0;
    width: 150px;
    height: 250px;
    background: radial-gradient(ellipse at 100% 40%, var(--wash-pink) 0%, var(--wash-light) 55%, rgba(244,163,182,0) 78%);
  }
  .contact-details {
    position: absolute;
    left: 48px;
    top: 48px;
    font-family: "PT Sans Narrow", "Arial Narrow", sans-serif;
    color: var(--ink);
    font-size: 17px;
    line-height: 1.55;
  }
  .person-name {
    font-family: "PT Serif", Georgia, serif;
    font-weight: 700;
    font-size: 22px;
    letter-spacing: 0.5px;
    color: var(--brand-red);
    text-transform: uppercase;
    line-height: 1.3;
  }
  .person-role { text-transform: uppercase; margin-bottom: 4px; }
  .company-address {
    position: absolute;
    left: 48px;
    bottom: 34px;
    font-family: "PT Sans Narrow", "Arial Narrow", sans-serif;
    font-size: 17px;
    text-transform: uppercase;
    color: var(--ink);
  }

  /* Brand side */
  .website {
    position: absolute;
    top: 22px;
    left: 26px;
    font-family: "PT Sans Narrow", "Arial Narrow", sans-serif;
    font-size: 15px;
    color: var(--muted);
  }
  .brand-lockup {
    position: absolute;
    right: 46px;
    top: 92px;
    display: flex;
    flex-direction: column;
    align-items: flex-end;
  }
  .brand-row { display: flex; align-items: center; gap: 16px; }
  .brand-dot {
    width: 96px;
    height: 96px;
    border-radius: 50%;
    background: var(--wash-pink);
  }
  .brand-name {
    font-family: "PT Serif", Georgia, serif;
    font-weight: 700;
    font-size: 64px;
    color: var(--brand-red);
    line-height: 1;
  }
  .brand-tagline {
    margin-top: 12px;
    font-family: "PT Serif", Georgia, serif;
    font-size: 20px;
    color: var(--muted);
    letter-spacing: 0.5px;
  }
</style>
</head>
<body>
  <section class="card card-contact">
    <div class="contact-wash" role="img" aria-label="Soft pink watercolour wash"></div>
    <div class="contact-details">
      <p class="person-name">Clara Whitfield</p>
      <p class="person-role">Director</p>
      <p class="person-phone">415-555-0187</p>
      <p class="person-email">clara@briskloom.com</p>
    </div>
    <p class="company-address">62 Harbor Lane, Oakridge CA 94500</p>
  </section>

  <section class="card card-brand">
    <p class="website">www.briskloom.com</p>
    <div class="brand-lockup">
      <div class="brand-row">
        <span class="brand-dot"></span>
        <span class="brand-name">Brisk</span>
      </div>
      <p class="brand-tagline">Yoga • Swim • Pole</p>
    </div>
  </section>
</body>
</html>
```